Thermal Camera flyer

We would like to obtain a sales orientated brochure to promote our two models of thermal imaging cameras as a response to the current Covid 19 health issues. I have provided the text, photos and detailed product specifications , in addition to a sample competitors brochure.
BROCHURE Details : 2 sided - front side to show product, its applications in business, school, hospitals, with text details - Back page to show specifications chart and contact information for Corvel Signal Works. (Melbourne -Sydney-Perth-Brisbane - 1300 647 519
Brochure should be "eye-catching" and reflect the product as a high quality, must-have technology device for todays world.

```html
<!DOCTYPE html>
<html lang="en">
<head>
<meta charset="utf-8">
<title>Thermal Camera Flyer</title>
<link rel="stylesheet" href="https://fonts.googleapis.com/css2?family=Poppins:wght@300;500;600&family=Roboto+Condensed:wght@300;400;700&display=swap">
<style>
  :root {
    --stage: #e9e8e4;
    --paper: #e4e2d7;
    --ink-dark: #29262f;
    --navy: #2f2b6e;
    --yellow-bright: #f2e413;
    --yellow-soft: #d9cd3a;
    --text: #2b2a2e;
    --call-blue: #2a57b3;
    --white: #ffffff;
    --photo-a: #3a3d46;
    --photo-b: #b9bcc4;
  }
  * { box-sizing: border-box; margin: 0; padding: 0; }
  html, body { width: 1200px; height: 1200px; overflow: hidden; background: var(--stage); }
  body { position: relative; font-family: "Roboto Condensed", sans-serif; color: var(--text); }

  .page {
    position: absolute; top: 218px; width: 540px; height: 764px;
    background: var(--paper); overflow: hidden;
    box-shadow: 0 6px 24px rgba(0,0,0,.15);
  }
  .page--front { left: 40px; }
  .page--back { left: 620px; }
  .page__shapes { position: absolute; inset: 0; width: 100%; height: 100%; }
  .page > *:not(.page__shapes) { position: absolute; }

  .photo { border-radius: 10px; }
  .photo--desk { left: 64px; top: 100px; width: 150px; height: 340px;
    background: linear-gradient(180deg, var(--photo-b) 0%, var(--photo-a) 55%, #15161a 100%); }
  .photo--floor { left: 262px; top: 470px; width: 90px; height: 260px;
    background: linear-gradient(180deg, var(--photo-a) 0%, var(--photo-b) 60%, #d6d7dc 100%); }
  .photo--stand { left: 228px; top: 70px; width: 80px; height: 500px;
    background: linear-gradient(180deg, var(--photo-a) 0%, var(--photo-b) 30%, #d3d4d9 85%, #8d9098 100%); }

  .caption { font-size: 7px; color: #555; }
  .caption--desk { left: 70px; top: 446px; }
  .caption--stand { left: 232px; top: 576px; }

  .title {
    left: 248px; top: 108px; width: 260px;
    font-family: "Poppins", sans-serif; font-weight: 500;
    font-size: 35px; line-height: 1.08; color: var(--white);
  }

  .lead {
    left: 40px; top: 470px; width: 210px;
    font-family: "Poppins", sans-serif; font-weight: 300;
    font-size: 12px; line-height: 1.3; color: var(--text);
  }

  .detail { left: 390px; top: 420px; width: 130px; font-size: 8px; line-height: 1.3; }
  .detail h3 { font-size: 8.5px; font-weight: 700; margin: 0 0 4px; }
  .detail p { margin: 0 0 5px; }

  .call {
    font-family: "Poppins", sans-serif; font-weight: 600;
    font-size: 17px; color: var(--call-blue); white-space: nowrap;
  }
  .page--front .call { left: 365px; top: 712px; }
  .page--back .call { left: 190px; top: 700px; }

  .brand { display: flex; align-items: center; gap: 8px;
    font-family: "Poppins", sans-serif; font-weight: 500; font-size: 13px; color: var(--text); }
  .brand__mark { width: 14px; height: 14px; background: var(--call-blue); }
  .page--front .brand { left: 40px; top: 712px; }
  .page--back .brand { left: 330px; top: 520px; font-size: 11px; }

  .locations { left: 352px; top: 540px; font-size: 8px; line-height: 1.4; }

  .spec-title {
    left: 170px; top: 40px; font-family: "Poppins", sans-serif; font-weight: 300;
    font-size: 17px; color: var(--white);
  }
  .specs { top: 150px; width: 190px; font-size: 8px; line-height: 1.4; }
  .specs--left { left: 28px; text-align: right; }
  .specs--right { left: 326px; }
  .specs h4 { font-size: 8.5px; font-weight: 700; margin: 8px 0 2px; }
  .specs ul { list-style: none; }
</style>
</head>
<body>

<section class="page page--front">
  <svg class="page__shapes" viewBox="0 0 540 764" aria-hidden="true">
    <path fill="var(--navy)" d="M0 0 H540 V300 C460 400 300 430 150 410 C90 400 40 380 0 360 Z"/>
    <path fill="var(--ink-dark)" d="M0 0 H540 V240 C470 350 300 385 150 368 C90 360 40 345 0 330 Z"/>
    <path fill="var(--yellow-bright)" d="M0 330 C40 345 90 360 150 368 C120 420 60 470 0 490 Z"/>
    <path fill="var(--yellow-soft)" d="M0 380 C60 376 110 372 150 368 C140 430 110 470 70 500 C40 490 15 470 0 460 Z"/>
    <circle cx="490" cy="830" r="240" fill="var(--yellow-soft)"/>
  </svg>

  <div class="photo photo--desk" role="img" aria-label="Photo of the desktop thermal scanning camera on its base, showing a masked visitor on screen"></div>
  <p class="caption caption--desk">Portable Camera on a Reception Desk</p>

  <h1 class="title">Thermal Scanning and Facial Recognition Camera</h1>

  <div class="detail">
    <h3>The Purpose of Thermal Scanning &amp; Facial Recognition</h3>
    <p>This system is designed to screen people as they enter a building, flagging anyone with an elevated skin temperature before they reach staff or students.</p>
    <p>The camera pairs a calibrated thermal sensor with facial recognition, so readings are matched to a face in under a second. Alerts sound when a reading passes a set limit, and mask detection can be switched on for extra safety.</p>
    <h3>Where and how can it be used?</h3>
    <p>Schools, hospitals, offices, factories and retail stores can place the unit at any entry point. It stands alone on a floor stand or mounts to a wall or turnstile.</p>
    <p>Our team can install, configure and support the system across Melbourne, Sydney, Perth and Brisbane, so you can protect your people with confidence.</p>
  </div>

  <p class="lead">The temperature of your body is no longer considered private information. That's the sea-change that businesses around the world are facing, as they install thermal imaging cameras for the safety of staff and visitors, often equipped with facial recognition technology, in their buildings to cope with the COVID-19 pandemic. It's a movement one might call the automation of temperature checks.</p>

  <div class="photo photo--floor" role="img" aria-label="Photo of the floor-standing thermal camera showing a visitor on screen"></div>

  <div class="brand"><span class="brand__mark"></span>Corvel Signal Works</div>
  <p class="call">Call : 1300 647 519</p>
</section>

<section class="page page--back">
  <svg class="page__shapes" viewBox="0 0 540 764" aria-hidden="true">
    <path fill="var(--navy)" d="M0 0 H540 V60 C430 150 250 170 0 120 Z"/>
    <path fill="var(--ink-dark)" d="M0 0 H540 V20 C430 110 250 130 0 90 Z"/>
    <path fill="var(--yellow-soft)" d="M0 300 C40 320 60 360 60 400 C40 420 20 430 0 432 Z"/>
    <path fill="var(--yellow-soft)" d="M0 764 V650 C120 610 400 600 540 650 V764 Z"/>
  </svg>

  <h2 class="spec-title">Technical Specifications</h2>

  <div class="specs specs--left">
    <h4>Hardware</h4>
    <ul>
      <li>Display: 8 inch IPS LCD</li>
      <li>Camera: dual lens 2MP</li>
      <li>Type: binocular live detection</li>
      <li>Fill light: LED and infrared</li>
      <li>Mount: floor, wall or desk</li>
    </ul>
    <h4>Screen</h4>
    <ul>
      <li>Size: 8 inch, 800 x 1280</li>
      <li>Touch: capacitive</li>
    </ul>
    <h4>Processor</h4>
    <ul>
      <li>CPU: quad core 1.8 GHz</li>
      <li>Storage: 16 GB</li>
    </ul>
    <h4>Interface</h4>
    <ul>
      <li>Network: RJ45, Wi-Fi</li>
      <li>Output: relay, Wiegand</li>
      <li>USB: 1 port</li>
      <li>Power: DC 12V 2A</li>
    </ul>
  </div>

  <div class="photo photo--stand" role="img" aria-label="Photo of the floor-standing thermal camera on its pole and base"></div>
  <p class="caption caption--stand">Floor-standing Camera</p>

  <div class="specs specs--right">
    <h4>Function</h4>
    <ul>
      <li>Face recognition in 0.2 s</li>
      <li>Mask detection with voice alert</li>
      <li>Live body detection</li>
      <li>Stores up to 20,000 faces</li>
      <li>Visitor and staff records</li>
      <li>Remote cloud management</li>
    </ul>
    <h4>IR Thermal Imaging Module</h4>
    <ul>
      <li>Range: 30 to 45°C</li>
      <li>Accuracy: ±0.3°C</li>
      <li>Distance: 0.5 to 1.2 m</li>
      <li>Response time: under 1 s</li>
      <li>Alarm on high reading</li>
    </ul>
  </div>

  <div class="brand"><span class="brand__mark"></span>Corvel Signal Works</div>
  <p class="locations">Melbourne · Sydney · Perth · Brisbane<br>www.corvelsignalworks.com.au</p>

  <p class="call">Call : 1300 647 519</p>
</section>

</body>
</html>
```